Business card for law firm

Need business card for new law firm. Think confident, authoritative, conservative, but not stuffy or old-fashioned.

Contact Information for Business Card

Content for card - logo (uploaded), plus the following:

Paul Wexbury (larger font)
Managing Partner (larger font, but not as large as name)
Level 9, 41 Tansy Lane
Sydney NSW 2000
Main Tel 02 7346 2190
Direct Tel 02 6273 4415
Email paul@qvlegal.com.au
www.qvlegal.com.au

Letterhead design should include logo plus:
Level 9, 41 Tansy Lane
Sydney NSW 2000
Tel 02 6273 4415
www.qvlegal.com.au

```html
<!DOCTYPE html>
<html lang="en">
<head>
<meta charset="utf-8">
<title>Quinvale Legal — Business Card</title>
<link href="https://fonts.googleapis.com/css2?family=Open+Sans:wght@800&family=Questrial&display=swap" rel="stylesheet">
<style>
  :root {
    --page: #ffffff;
    --card: #201a19;
    --ink-light: #ffffff;
    --accent: #d8312f;
    --rule: #8a8584;
  }
  * { margin: 0; padding: 0; box-sizing: border-box; }
  html, body {
    width: 1200px; height: 1200px; overflow: hidden;
    background: var(--page);
  }
  .canvas { position: relative; width: 1200px; height: 1200px; }
  .card {
    position: absolute; left: 210px; width: 699px; height: 474px;
    background: var(--card); border-radius: 30px;
  }
  .card--front { top: 93px; }
  .card--back { top: 614px; }
  .abs { position: absolute; }

  /* Front */
  .brand-mark { background: var(--ink-light); }
  .card--front .brand-mark { left: 279px; top: 62px; width: 136px; height: 136px; }
  .brand-name {
    font-family: "Questrial", sans-serif; font-weight: 400;
    text-align: center; white-space: nowrap;
  }
  .card--front .brand-name {
    left: 0; width: 699px; top: 240px; color: var(--ink-light);
  }
  .brand-name__main { display: block; font-size: 62px; line-height: 1; letter-spacing: 0.04em; }
  .card--front .brand-name__sub { display: block; font-size: 32px; letter-spacing: 0.55em; margin-top: 14px; padding-left: 0.55em; }
  .front-url {
    left: 0; width: 699px; top: 430px; text-align: center;
    font-family: "Questrial", sans-serif; font-size: 20px; letter-spacing: 0.34em;
    color: var(--ink-light);
  }

  /* Back */
  .card--back .brand-mark { left: 125px; top: 136px; width: 92px; height: 92px; background: var(--accent); }
  .card--back .brand-name { left: 40px; width: 262px; top: 256px; color: var(--accent); }
  .card--back .brand-name__main { font-size: 38px; letter-spacing: 0.03em; }
  .card--back .brand-name__sub { display: block; font-size: 21px; letter-spacing: 0.55em; margin-top: 10px; padding-left: 0.55em; }
  .divider { left: 344px; top: 104px; width: 1px; height: 282px; background: var(--rule); }
  .person { left: 390px; top: 110px; }
  .person__name {
    font-family: "Open Sans", sans-serif; font-weight: 800; font-size: 32px;
    line-height: 1.1; color: var(--accent); white-space: nowrap;
  }
  .person__title {
    font-family: "Questrial", sans-serif; font-size: 11px; letter-spacing: 0.2em;
    color: var(--ink-light); text-align: center; margin-top: 3px;
  }
  .contact {
    left: 390px; font-family: "Questrial", sans-serif; font-size: 21px;
    line-height: 27px; color: var(--ink-light); white-space: nowrap;
    -webkit-text-stroke: 0.4px var(--ink-light);
  }
  .contact--address { top: 188px; }
  .contact--lines { top: 271px; }
  .contact__hl { color: var(--accent); -webkit-text-stroke: 0.4px var(--accent); }
</style>
</head>
<body>
<main class="canvas">
  <section class="card card--front" aria-label="Card front">
    <div class="abs brand-mark"></div>
    <div class="abs brand-name">
      <span class="brand-name__main">QUINVALE</span>
      <span class="brand-name__sub">LEGAL</span>
    </div>
    <p class="abs front-url">WWW.QVLEGAL.COM.AU</p>
  </section>

  <section class="card card--back" aria-label="Card back">
    <div class="abs brand-mark"></div>
    <div class="abs brand-name">
      <span class="brand-name__main">QUINVALE</span>
      <span class="brand-name__sub">LEGAL</span>
    </div>
    <div class="abs divider"></div>
    <div class="abs person">
      <p class="person__name">Paul Wexbury</p>
      <p class="person__title">MANAGING PARTNER</p>
    </div>
    <p class="abs contact contact--address">Level 9, 41 Tansy Lane<br>Sydney NSW 2000</p>
    <p class="abs contact contact--lines">
      Main Tel 02 7346 2190<br>
      Direct Tel 02 6273 4415<br>
      Email paul@qvlegal.com.au<br>
      www.<span class="contact__hl">qvlegal</span>.com.au
    </p>
  </section>
</main>
</body>
</html>
```